Flyer-Design für KL Kurier
Zielgruppe
Wir transportieren Dokumente, Pakete, Sperrgut und Paletten weltweit per Luftfracht. Unsere Zielgruppe sind Firmenkunden bis 300 Mitarbeiter die internationalen Versand haben.
Aufgabenstellung
Der Flyer soll DIN A 5 sein, beide Seiten bedruckt. Der Kunde soll den Flyer an seine Schreibtischunterlage legen, an die Pinnwand heften, auf jeden Fall aufheben. Dazu können Sie auch eine Stanzform gestalten. Uns soll der Kunden anrufen, wenn er Probleme hat. Das kann sein: Die Laufzeit(Liefergeschwindigkeit) von seinem jetzigen Anbieter ist zu langsam oder sein jetziger Anbieter kann den Transport gar nicht durchführen. Also immer, wenn Probleme auftreten oder der Transport mehr als 300 Euro kostet, dann soll der Kunden uns anrufen. Wir sind quasi die Transportfeuerwehr und helfen, wenn es brennt. Das heißt, dass der Kunden uns nicht täglich nutzen. Das muss im Flyer klarwerden. „Ich hebe den Flyer auf und wenn es brennt, rufe ich bei KL Kurier an, die helfen mir weiter.“ Vielleicht integrieren Sie einen Feuermelder oder ähnliches.
Wir haben auch festgestellt, dass Kunden Flyer die gefalzt sind oder größer als A5 nicht aufheben.

```html
<!DOCTYPE html>
<html lang="de">
<head>
<meta charset="utf-8">
<title>KL Kurier – Flyer A5</title>
<link rel="stylesheet" href="https://fonts.googleapis.com/css2?family=Roboto+Condensed:wght@400;700;800&family=Roboto:wght@300;400;700&display=swap">
<style>
  :root {
    --bg: #d9d9d9;
    --paper: #ffffff;
    --green: #6ab04c;
    --yellow: #f2ea2c;
    --red: #d4231c;
    --ink: #1d1d1b;
    --fire-1: #f6b13a;
    --fire-2: #d9521c;
    --fire-3: #6b1f10;
  }
  * { box-sizing: border-box; margin: 0; padding: 0; }
  html, body { width: 1200px; height: 1200px; overflow: hidden; }
  body {
    background: var(--bg);
    display: flex;
    flex-direction: column;
    align-items: center;
    justify-content: center;
    gap: 40px;
    font-family: "Roboto", Arial, sans-serif;
  }
  .flyer {
    position: relative;
    width: 780px;
    height: 552px;
    background: var(--paper);
    overflow: hidden;
    box-shadow: 0 6px 18px rgba(0,0,0,.25);
  }

  /* Front side */
  .front .edge-photo {
    position: absolute; left: 0; top: 0; width: 40px; height: 100%;
    background: linear-gradient(180deg, #3a1a0e 0%, #7a2e12 55%, #2a120a 100%);
  }
  .front .bar-left { position: absolute; left: 40px; top: 0; width: 20px; height: 100%; background: var(--green); }
  .front .bar-mid { position: absolute; left: 362px; top: 0; width: 16px; height: 100%; background: var(--green); }
  .front .hero-photo {
    position: absolute; left: 378px; top: 0; right: 0; height: 408px;
    background: radial-gradient(ellipse at 55% 45%, var(--fire-1) 0%, var(--fire-2) 50%, var(--fire-3) 100%);
  }
  .front .headline {
    position: absolute; left: 78px; top: 92px; width: 278px;
    font-family: "Roboto Condensed", Arial, sans-serif;
    font-weight: 800; font-size: 38px; line-height: 1.05;
    color: var(--red);
    text-shadow: -2px -2px 0 #fff, 2px -2px 0 #fff, -2px 2px 0 #fff, 2px 2px 0 #fff, 0 2px 0 #fff, 0 -2px 0 #fff, 4px 5px 6px rgba(0,0,0,.45);
  }
  .front .hotline {
    position: absolute; left: 78px; top: 196px;
    font-family: "Roboto Condensed", Arial, sans-serif;
    font-weight: 800; font-size: 36px; color: var(--red);
    text-shadow: -2px -2px 0 #fff, 2px -2px 0 #fff, -2px 2px 0 #fff, 2px 2px 0 #fff, 4px 5px 6px rgba(0,0,0,.45);
  }
  .front .benefits { position: absolute; left: 78px; top: 312px; list-style: none; }
  .front .benefits li {
    display: flex; align-items: center; gap: 10px;
    font-family: "Roboto Condensed", Arial, sans-serif;
    font-weight: 700; font-size: 13.5px; color: var(--ink);
    height: 34px;
  }
  .front .benefits svg { width: 13px; height: 13px; flex: none; }
  .brand {
    position: absolute; display: flex; align-items: center; gap: 14px;
    font-family: "Roboto Condensed", Arial, sans-serif; font-weight: 800;
    color: var(--ink); letter-spacing: .5px;
  }
  .brand .brand-mark { background: var(--green); flex: none; }
  .front .brand { left: 430px; top: 448px; font-size: 52px; }
  .front .brand .brand-mark { width: 38px; height: 38px; }

  /* Back side */
  .back .stripe-a { position: absolute; left: 0; top: 0; width: 16px; height: 100%; background: var(--yellow); }
  .back .panel { position: absolute; left: 16px; top: 0; width: 300px; height: 100%; background: var(--green); }
  .back .stripe-b { position: absolute; left: 316px; top: 0; width: 16px; height: 100%; background: var(--yellow); }
  .back .contact {
    position: absolute; left: 74px; top: 376px; color: #fff; font-style: normal;
    font-family: "Roboto Condensed", Arial, sans-serif; font-size: 13px; line-height: 1.55;
  }
  .back .contact .name { font-weight: 700; margin-bottom: 8px; }
  .back .contact .block { margin-bottom: 8px; }
  .back .title {
    position: absolute; left: 392px; top: 110px;
    font-family: "Roboto Condensed", Arial, sans-serif; font-weight: 700;
    font-size: 30px; line-height: 1.15; color: var(--ink);
  }
  .back .services { position: absolute; left: 392px; top: 222px; list-style: none; }
  .back .services li {
    display: flex; align-items: center; gap: 12px;
    font-family: "Roboto", Arial, sans-serif; font-weight: 300;
    font-size: 19px; color: var(--ink); height: 36px; letter-spacing: .5px;
  }
  .back .services .bullet { width: 12px; height: 12px; background: var(--green); flex: none; }
  .back .brand { left: 470px; top: 438px; font-size: 54px; }
  .back .brand .brand-mark { width: 40px; height: 40px; }
</style>
</head>
<body>

  <section class="flyer front" aria-label="Flyer Vorderseite">
    <div class="edge-photo" role="img" aria-label="Randausschnitt des Feuerwehr-Fotos"></div>
    <div class="bar-left"></div>
    <div class="bar-mid"></div>
    <div class="hero-photo" role="img" aria-label="Foto: Feuerwehrmann mit Helm, Atemschutz und Werkzeug vor Flammen"></div>

    <h1 class="headline">Wenn es brennt,<br>rufen Sie uns an!</h1>
    <p class="hotline">0711/4820935</p>

    <ul class="benefits">
      <li><svg viewBox="0 0 12 12"><path d="M1 6.5 L4.5 10 L11 1.5" fill="none" stroke="var(--green)" stroke-width="2"/></svg>Wir helfen Ihnen bei Transportproblemen</li>
      <li><svg viewBox="0 0 12 12"><path d="M1 6.5 L4.5 10 L11 1.5" fill="none" stroke="var(--green)" stroke-width="2"/></svg>Heute abgeholt und heute noch zugestellt</li>
      <li><svg viewBox="0 0 12 12"><path d="M1 6.5 L4.5 10 L11 1.5" fill="none" stroke="var(--green)" stroke-width="2"/></svg>Zustellung in den USA am nächsten Tag</li>
      <li><svg viewBox="0 0 12 12"><path d="M1 6.5 L4.5 10 L11 1.5" fill="none" stroke="var(--green)" stroke-width="2"/></svg>Weltweiter Transport</li>
      <li><svg viewBox="0 0 12 12"><path d="M1 6.5 L4.5 10 L11 1.5" fill="none" stroke="var(--green)" stroke-width="2"/></svg>Erstellung Ihrer Exportpapiere</li>
      <li><svg viewBox="0 0 12 12"><path d="M1 6.5 L4.5 10 L11 1.5" fill="none" stroke="var(--green)" stroke-width="2"/></svg>Bester Kundendienst</li>
    </ul>

    <div class="brand"><span class="brand-mark"></span>KL Kurier</div>
  </section>

  <section class="flyer back" aria-label="Flyer Rückseite">
    <div class="stripe-a"></div>
    <div class="panel"></div>
    <div class="stripe-b"></div>

    <address class="contact">
      <p class="name">KL Kurier</p>
      <p class="block">Lindenweg 7<br>70173 Beispielstadt</p>
      <p>post@kl-kurier.de<br>Tel. 0711/4820935</p>
    </address>

    <h2 class="title">Weltweiter Transport<br>per Luftfracht</h2>
    <ul class="services">
      <li><span class="bullet"></span>DOKUMENTE</li>
      <li><span class="bullet"></span>PAKETE</li>
      <li><span class="bullet"></span>SPERRGUT</li>
      <li><span class="bullet"></span>PALETTEN</li>
    </ul>

    <div class="brand"><span class="brand-mark"></span>KL Kurier</div>
  </section>

</body>
</html>
```